New Bicycle shop business card

Hi!
I'm looking for a business card for my new proffesional bike mechanics shop. This shop is only for fixing broken bikes and not selling bikes.
Peferbly a modern and sleek and modern design.
Colors: black, grey, red, white
Information:
Name: Rijwielwerkplaats Vanhoutem
Shop owner: Bart Vanhoutem & Sanne Maertens
Website: www.rijwielwerkplaats-vanhoutem.be
Email: info@rijwielwerkplaats-vanhoutem.be
Phone number: +32471902386
Street adres: Kerkweg 64
9970 Oostmoere
Slogan/shop information: Herstellingen van alle merken.
Logo: see files.
Target Market(s)
People who seek a mechanic to fix or upgrade their bikes.
Contact Information for Business Card
Information:
Website: info@rijwielwerkplaats-vanhoutem.be
9970 Oostmoere
Logo: see files.

```html
<!DOCTYPE html>
<html lang="nl">
<head>
<meta charset="utf-8">
<title>Rijwielwerkplaats Vanhoutem – visitekaartje</title>
<link rel="stylesheet" href="https://fonts.googleapis.com/css2?family=Montserrat:wght@500;600;700&display=swap">
<style>
  :root {
    --bg: #2e3b42;
    --black: #050505;
    --white: #ffffff;
    --red: #d91f3d;
    --grey: #b9b9b9;
    --ink: #111111;
  }
  * { box-sizing: border-box; margin: 0; padding: 0; }
  html, body { width: 1200px; height: 1200px; overflow: hidden; }
  body {
    background: var(--bg);
    font-family: "Montserrat", sans-serif;
    position: relative;
  }
  .card {
    position: absolute;
    left: 150px;
    width: 900px;
    height: 500px;
    box-shadow: 0 18px 40px rgba(0,0,0,.45);
  }
  .card-front {
    top: 60px;
    background: var(--black);
    display: flex;
    flex-direction: column;
    align-items: center;
    justify-content: center;
  }
  .brand {
    display: flex;
    align-items: center;
    gap: 18px;
  }
  .brand-mark {
    width: 22px;
    height: 22px;
    background: var(--red);
    flex: none;
  }
  .brand-name {
    color: var(--white);
    font-weight: 700;
    text-transform: uppercase;
    line-height: 1.15;
    letter-spacing: .06em;
  }
  .card-front .brand-name { font-size: 38px; }
  .slogan {
    margin-top: 70px;
    color: var(--white);
    font-weight: 600;
    font-size: 21px;
    letter-spacing: .2em;
  }
  .card-back {
    top: 640px;
    display: flex;
  }
  .back-brand {
    width: 50%;
    background: var(--black);
    display: flex;
    align-items: center;
    justify-content: center;
    padding: 0 30px;
  }
  .card-back .brand-name { font-size: 26px; }
  .back-contact {
    width: 50%;
    background: var(--white);
    position: relative;
    padding: 135px 30px 0 42px;
    color: var(--ink);
  }
  .divider-tab {
    position: absolute;
    left: 0;
    top: 130px;
    width: 24px;
    height: 56px;
    background: var(--black);
  }
  .owners {
    font-weight: 600;
    font-size: 19px;
    letter-spacing: .03em;
  }
  .role {
    margin-top: 4px;
    color: var(--red);
    font-weight: 600;
    font-size: 16px;
    letter-spacing: .03em;
  }
  .contact-list {
    list-style: none;
    margin-top: 58px;
  }
  .contact-item {
    display: flex;
    align-items: flex-start;
    gap: 18px;
    font-weight: 600;
    font-size: 19px;
    letter-spacing: .05em;
    line-height: 1.4;
    margin-bottom: 16px;
  }
  .contact-item svg { flex: none; margin-top: 2px; }
</style>
</head>
<body>
  <section class="card card-front">
    <div class="brand">
      <span class="brand-mark"></span>
      <div class="brand-name">Rijwielwerkplaats<br>Vanhoutem</div>
    </div>
    <p class="slogan">Herstellingen van alle merken</p>
  </section>

  <section class="card card-back">
    <div class="back-brand">
      <div class="brand">
        <span class="brand-mark"></span>
        <div class="brand-name">Rijwielwerkplaats<br>Vanhoutem</div>
      </div>
    </div>
    <div class="back-contact">
      <span class="divider-tab"></span>
      <p class="owners">Bart Vanhoutem &amp; Sanne Maertens</p>
      <p class="role">Shop owner</p>
      <ul class="contact-list">
        <li class="contact-item">
          <svg width="26" height="24" viewBox="0 0 26 24" aria-hidden="true">
            <path d="M13 1 L1 12 H4 V23 H10 V16 H16 V23 H22 V12 H25 Z" fill="var(--red)"/>
          </svg>
          <span>Kerkweg 64 9970<br>Oostmoere</span>
        </li>
        <li class="contact-item">
          <svg width="26" height="28" viewBox="0 0 26 28" aria-hidden="true">
            <rect x="6" y="1" width="14" height="26" rx="2" fill="none" stroke="var(--red)" stroke-width="2.4"/>
            <line x1="11" y1="23" x2="15" y2="23" stroke="var(--red)" stroke-width="2"/>
          </svg>
          <span>+32471902386</span>
        </li>
      </ul>
    </div>
  </section>
</body>
</html>
```